Colin Vesk Personal Card

I am looking for a personal card that has my contact information on the front and then the url for my website on the back. I am a fan of minimal, modern design, but am very open minded to other styles. Both portrait and landscape designs are acceptable. The only other specification that I have is that some sort of graphic of a raven is present somewhere on the card (my last name 'Vesk' means raven in German).
Industry/Entity Type
Landscape
Contact Information for Business Card
Colin Vesk
508.641.2093
colintvesk@postvale.com
colintvesk.com
Colors
Designer to choose colors to be used in the design.
Requirements
Must have
- Raven on some part of the card

```html
<!DOCTYPE html>
<html lang="en">
<head>
<meta charset="utf-8">
<title>Colin Vesk – Personal Card</title>
<link rel="stylesheet" href="https://fonts.googleapis.com/css2?family=Arimo:wght@400;700&display=swap">
<style>
  :root {
    --backdrop: #dcdcdc;
    --teal-deep: #176882;
    --teal-bright: #1a87a3;
    --paper: #ffffff;
    --ink: #222222;
    --ink-soft: #333333;
    --mist: #ececec;
  }
  * { margin: 0; padding: 0; box-sizing: border-box; }
  html, body {
    width: 1200px; height: 840px; overflow: hidden;
    background: var(--backdrop);
    font-family: "Arimo", Arial, sans-serif;
  }
  .canvas { position: relative; width: 1200px; height: 840px; }

  .card { position: absolute; width: 470px; height: 272px; overflow: hidden; }

  /* Back of card */
  .card--back { left: 87px; top: 274px; background: var(--teal-deep); color: var(--paper); }
  .card--back .brand { position: absolute; left: 230px; top: 168px; display: flex; align-items: center; gap: 14px; }
  .card--back .brand-dot { width: 54px; height: 54px; border-radius: 50%; background: var(--paper); }
  .card--back .brand-name { font-size: 37px; line-height: 1; letter-spacing: 0.5px; }
  .card--back .brand-url { font-size: 12.5px; margin-top: 3px; }

  /* Front of card */
  .card--front { left: 645px; top: 273px; background: var(--paper); }
  .bird-shade {
    position: absolute; left: 0; top: 0; width: 170px; height: 142px;
    background: radial-gradient(ellipse at 50% 40%, var(--mist) 0%, rgba(236,236,236,0.7) 50%, rgba(255,255,255,0) 72%);
  }
  .card--front .brand { position: absolute; right: 38px; top: 38px; display: flex; flex-direction: column; align-items: center; gap: 10px; }
  .card--front .brand-dot { width: 46px; height: 46px; border-radius: 50%; background: var(--teal-bright); }
  .card--front .brand-name { font-size: 34px; line-height: 1; color: var(--ink); letter-spacing: 0.5px; }

  .holder-name {
    position: absolute; left: 37px; top: 186px;
    font-size: 31px; font-weight: 700; color: var(--teal-bright); letter-spacing: 0.3px;
  }
  .contact-row {
    position: absolute; left: 39px; right: 38px; top: 233px;
    display: flex; justify-content: space-between; list-style: none;
    font-size: 11.5px; color: var(--ink-soft);
  }
  .contact-item { display: flex; align-items: center; gap: 7px; }
  .contact-icon { width: 14px; height: 14px; flex: none; }
  .accent-band { position: absolute; left: 0; right: 0; bottom: 0; height: 8px; background: var(--teal-bright); }
</style>
</head>
<body>
<main class="canvas">

  <section class="card card--back" aria-label="Card back">
    <div class="brand">
      <span class="brand-dot"></span>
      <div>
        <div class="brand-name">VESK</div>
        <div class="brand-url">www.colintvesk.com</div>
      </div>
    </div>
  </section>

  <section class="card card--front" aria-label="Card front">
    <div class="bird-shade" role="img" aria-label="Faint large bird silhouette in flight"></div>

    <div class="brand">
      <span class="brand-dot"></span>
      <span class="brand-name">VESK</span>
    </div>

    <h1 class="holder-name">COLIN VESK</h1>

    <ul class="contact-row">
      <li class="contact-item">
        <svg class="contact-icon" viewBox="0 0 14 14" aria-hidden="true">
          <circle cx="7" cy="7" r="7" fill="#333"/>
          <rect x="4.8" y="3" width="4.4" height="8" rx="0.8" fill="none" stroke="#fff" stroke-width="1"/>
        </svg>
        508.641.2093
      </li>
      <li class="contact-item">
        <svg class="contact-icon" viewBox="0 0 14 14" aria-hidden="true">
          <circle cx="7" cy="7" r="7" fill="#333"/>
          <rect x="3.5" y="4.5" width="7" height="5" fill="#fff"/>
          <path d="M3.5 4.5 L7 7.3 L10.5 4.5" fill="none" stroke="#333" stroke-width="0.8"/>
        </svg>
        colintvesk@postvale.com
      </li>
      <li class="contact-item">
        <svg class="contact-icon" viewBox="0 0 14 14" aria-hidden="true">
          <circle cx="7" cy="7" r="7" fill="#333"/>
          <circle cx="7" cy="7" r="3.8" fill="#777"/>
        </svg>
        www.colintvesk.com
      </li>
    </ul>

    <div class="accent-band"></div>
  </section>

</main>
</body>
</html>
```